Solvane Vitality MediSpa Brochure

We need a new brochure design. The old is attached.

We are wanting a three panel brochure for med spa designed and ready for print. The brochure will have content and images on both sides. We attached the old brochure in pdf format. The content needs to stay as on the attached pdf but please feel free to offer new designs. The color needs to match the attached logo, which is a light blue and teal. All images we want on the brochure are also attached.

The design must have an 1/8 in space from each edge for printing purposes

Target Market(s)

Men and Women

Industry/Entity Type

Wellness

Font styles to use
Sans Serif

Colors
34a6d7
33b8a4

Requirements
Must have
• soft curves. must have a 1/8 in space on all edges (including interior) to give bleed space for printing. Use content written on attached brochure.

```html
<!DOCTYPE html>
<html lang="en">
<head>
<meta charset="utf-8">
<title>Solvane Vitality MediSpa – Trifold Brochure</title>
<link href="https://fonts.googleapis.com/css2?family=Source+Sans+3:wght@400;600;700&family=Alegreya+Sans:wght@500&display=swap" rel="stylesheet">
<style>
  :root{
    --teal:#17a3a6;
    --teal-dark:#0f9295;
    --charcoal:#4a4a4a;
    --charcoal-dark:#3d3d3d;
    --mist:#ececec;
    --paper:#ffffff;
    --ink:#222222;
    --ink-soft:#555555;
  }
  *{margin:0;padding:0;box-sizing:border-box}
  html,body{width:1200px;height:1200px;overflow:hidden;background:var(--paper)}
  body{font-family:"Source Sans 3",Arial,sans-serif;color:var(--ink)}
  .stage{position:relative;width:1200px;height:1200px;overflow:hidden;background:var(--paper)}
  .brochure{position:absolute;left:0;top:171px;width:1220px;height:872px;transform:scale(0.98361);transform-origin:0 0;overflow:hidden;background:var(--paper)}
  .backdrop{position:absolute;inset:0;width:1220px;height:872px}
  .txt{position:absolute}

  /* panel one */
  .intro-heading{left:60px;top:22px;font-size:19.5px;font-weight:700;color:var(--teal);letter-spacing:.2px}
  .intro-body{left:64px;top:58px;width:275px;font-size:13.4px;line-height:17px;color:var(--ink)}
  .intro-body p{margin-bottom:17px}
  .membership-list{left:66px;top:470px;list-style:none;font-size:15px;font-weight:600;color:var(--teal);line-height:19px}
  .membership-list li::before,.service-list li::before{content:"";display:inline-block;width:9px;height:9px;border-radius:50%;background:var(--teal);margin-right:8px;vertical-align:1px}
  .learn-more{left:49px;top:798px;font-size:14.5px;line-height:19px;color:var(--ink)}

  /* panel two */
  .location{left:412px;width:400px;top:46px;text-align:center;color:#fff;font-size:13.4px;line-height:17px}
  .location h2{font-size:23px;font-weight:700;color:var(--teal);text-decoration:underline;text-underline-offset:3px;margin-bottom:10px;line-height:26px}
  .location p{margin-bottom:17px}
  .doctor-name{left:495px;width:235px;top:500px;text-align:center;color:#fff;font-size:13.5px;font-weight:700;line-height:18px}
  .doctor-note{left:474px;top:583px;width:292px;color:#fff;font-size:13.4px;line-height:17px}
  .doctor-note p{margin-bottom:27px}

  /* panel three */
  .brand{left:835px;width:360px;top:62px;text-align:center;color:var(--teal);font-size:31px;font-weight:600;line-height:36px}
  .brand .dot{display:inline-block;width:14px;height:14px;border-radius:50%;background:var(--teal);margin-right:10px;vertical-align:4px}
  .tagline{left:805px;width:415px;top:163px;height:59px;text-align:center;font-family:"Alegreya Sans",sans-serif;font-weight:500;color:#fff;font-size:40px;line-height:59px}
  .audience{left:880px;top:618px;font-weight:600;line-height:1}
  .audience .line-a{display:block;font-size:47px;color:var(--charcoal);letter-spacing:.5px}
  .audience .line-b{display:block;font-size:61px;color:var(--teal);margin-top:-4px;letter-spacing:.5px}
  .service-list{top:731px;list-style:none;font-size:14.5px;line-height:19px;color:var(--ink)}
  .service-list.col-a{left:886px}
  .service-list.col-b{left:1028px}
  .contact-web{left:830px;width:380px;top:800px;text-align:center;font-size:15px;color:var(--teal);line-height:19px}
  .contact-phone{left:830px;width:380px;top:819px;text-align:center;font-size:15px;color:var(--ink-soft);line-height:19px}
</style>
</head>
<body>
<div class="stage">
  <div class="brochure">
    <svg class="backdrop" viewBox="0 0 1220 872" xmlns="http://www.w3.org/2000/svg">
      <defs>
        <linearGradient id="mistFade" x1="0" y1="0" x2="1" y2="0">
          <stop offset="0" stop-color="#e4e4e4"/><stop offset="1" stop-color="#f6f6f6"/>
        </linearGradient>
        <linearGradient id="charcoalFade" x1="0" y1="0" x2="1" y2="0">
          <stop offset="0" stop-color="#3f3f3f"/><stop offset="1" stop-color="#5e5e5e"/>
        </linearGradient>
        <linearGradient id="skinTone" x1="0" y1="0" x2="1" y2="1">
          <stop offset="0" stop-color="#f3d9cc"/><stop offset="0.6" stop-color="#e9bfa9"/><stop offset="1" stop-color="#d9a48c"/>
        </linearGradient>
        <linearGradient id="gardenTone" x1="0" y1="0" x2="0" y2="1">
          <stop offset="0" stop-color="#6fa655"/><stop offset="0.55" stop-color="#3e7a36"/><stop offset="1" stop-color="#2a3350"/>
        </linearGradient>
        <linearGradient id="portraitTone" x1="0" y1="0" x2="1" y2="1">
          <stop offset="0" stop-color="#f1f1f1"/><stop offset="0.5" stop-color="#e8c6b2"/><stop offset="1" stop-color="#d8ab93"/>
        </linearGradient>
        <linearGradient id="lowerFade" x1="0" y1="0" x2="0" y2="1">
          <stop offset="0" stop-color="#ededed"/><stop offset="1" stop-color="#ffffff"/>
        </linearGradient>
      </defs>

      <!-- panel one -->
      <rect x="0" y="0" width="412" height="872" fill="#ffffff"/>
      <path d="M0,0 H412 V478 C260,540 110,640 0,790 Z" fill="url(#mistFade)"/>
      <path d="M0,790 C110,640 260,540 412,478 L412,545 C250,590 90,690 0,805 Z" fill="url(#charcoalFade)"/>
      <path d="M0,805 C90,690 250,590 412,545 L412,556 C250,600 95,700 0,815 Z" fill="#ffffff"/>

      <!-- panel two -->
      <rect x="412" y="0" width="410" height="872" fill="#ffffff"/>
      <path d="M412,0 H818 C800,140 770,250 700,330 C620,410 520,455 412,478 Z" fill="url(#charcoalFade)"/>
      <path d="M412,497 C540,470 660,420 730,350 C770,305 786,275 795,262 C812,330 818,420 812,520 C805,650 790,760 752,858 L412,858 Z" fill="var(--teal)"/>
      <path d="M818,150 C825,300 830,460 820,590 C810,710 790,800 752,858 L772,858 C810,790 830,700 838,590 C845,460 838,300 818,150 Z" fill="var(--charcoal)"/>

      <!-- panel three -->
      <rect x="838" y="0" width="382" height="858" fill="#ffffff"/>
      <path d="M838,590 C835,700 822,790 772,858 H1220 V560 Z" fill="url(#lowerFade)"/>
      <rect x="805" y="163" width="415" height="59" fill="var(--teal)"/>
      <rect role="img" aria-label="Close-up photograph of a woman's face with clear glowing skin" x="795" y="226" width="425" height="330" fill="url(#skinTone)"/>
      <path d="M795,556 V226 H1220 V520 C1120,560 950,545 830,550 Z" fill="url(#skinTone)"/>
      <path d="M815,545 C960,520 1130,550 1220,635 L1220,560 C1130,520 960,515 815,545 Z" fill="var(--teal)"/>
      <path d="M815,545 C960,525 1130,555 1220,640 L1220,600 V856 H838 C838,720 830,620 815,545 Z" fill="url(#lowerFade)"/>

      <!-- photo circles -->
      <circle role="img" aria-label="Portrait photograph of a smiling woman in a garden" cx="612" cy="437" r="113" fill="url(#gardenTone)" stroke="#ffffff" stroke-width="6"/>
      <circle role="img" aria-label="Beauty photograph of a woman touching her neck" cx="188" cy="662" r="113" fill="url(#portraitTone)" stroke="var(--teal)" stroke-width="5"/>

      <!-- bottom bands -->
      <rect x="0" y="858" width="412" height="14" fill="var(--teal)"/>
      <rect x="412" y="858" width="340" height="14" fill="var(--charcoal)"/>
      <rect x="752" y="858" width="468" height="14" fill="var(--teal)"/>
    </svg>

    <!-- panel one -->
    <h1 class="txt intro-heading">LARKFIELD’S PREMIER MEDIA</h1>
    <div class="txt intro-body">
      <p>LARKFIELD’S PREMIER MEDISPA<br>Solvane Vitality MediSpa is the premier medical spa in Larkfield, TX. We utilize the best equipment available today for laser treatments, dermal fillers, facials, injections, chemical peels and wellness solutions.</p>
      <p>WHY CHOOSE OUR MEDISPA?<br>Under the supervision of Dr. Elena Marsh, our medical staff provides state-of-the-art cosmetic treatments to both women and men.</p>
      <p>Our staff is trained to provide unique medical spa services to help our clients achieve a more youthful look and defy the aging process.</p>
      <p>EXCLUSIVE MEMBERSHIPS<br>Our exclusive membership packages are tailored for our clients and created to give them an exceptional experience at a discounted price.</p>
    </div>
    <ul class="txt membership-list">
      <li>SILVER Membership</li>
      <li>GOLD Membership</li>
      <li>PLATINUM Membership</li>
    </ul>
    <p class="txt learn-more">Learn More At<br>www.SolvaneVitalityMedispa.com/memberships</p>

    <!-- panel two -->
    <div class="txt location">
      <h2>LOCATION</h2>
      <p>742 W. Larkfield Blvd<br>Suite 210<br>Larkfield TX 75014</p>
      <p>SCHEDULE A CONSULTATION</p>
      <p>Ph: (555) 014-2280</p>
      <p>Fax: (555) 014-2291<br>refreshedface@elenamarshmd.com</p>
      <p>www.SolvaneVitalityMedispa.com</p>
    </div>
    <p class="txt doctor-name">DR. ELENA MARSH<br>MD. FACS</p>
    <div class="txt doctor-note">
      <p>Rejuvenation and reconstruction of the face are my passion, whether it is to improve one’s visual functions or to enhance one’s appearance.</p>
      <p>I personally perform all of my injections and Co2 laser treatments because safety and satisfaction are my top priorities.</p>
      <p>I was called by God to become a physician at the age of seven years old. I am motivated by a desire to serve others by providing superb medical care. I constantly strive to do my best.</p>
    </div>

    <!-- panel three -->
    <p class="txt brand"><span class="dot"></span>Solvane Vitality<br>MediSpa</p>
    <p class="txt tagline">Refresh &amp; Rejuvenate</p>
    <p class="txt audience"><span class="line-a">FOR WOMEN</span><span class="line-b">AND MEN</span></p>
    <ul class="txt service-list col-a">
      <li>Laser Treatments</li>
      <li>Dermal Fillers</li>
      <li>Neurotoxins</li>
    </ul>
    <ul class="txt service-list col-b">
      <li>Facials</li>
      <li>Chemical Peels</li>
      <li>Wellness Treatments</li>
    </ul>
    <p class="txt contact-web">www.SolvaneVitalityMedispa.com</p>
    <p class="txt contact-phone">(555) 014-2280</p>
  </div>
</div>
</body>
</html>
```